MOSLEN Environmental needs an upgrade to its current business cards design

We need an upgrade to our current business cards design, where the MOSLEN acronym is included, as possible and not being overloaded.
MOSLEN Environmental is an Environmental Consultancy Firm based in Sydney.
We would like to see creative designs different from the standard type of business cards (for example, rounded edges, different to standard size of common business cards.

Target Market(s)

industrial companies (oil & gas, petrochemical, mining, insolvency, finance and manufacturing), developers, architect firms, law firms.

Industry/Entity Type

Business

Contact Information for Business Card

logos (brand and acronym), if they don't appear overloaded.
name
role
name of company (MOSLEN Environmental),
address (Level 3, Suite 3C, 47-49 Dorrigan Lane, Wexmoor, NSW, 2188) landline (02 7314 2986)
mobile (staff member)
email (staff member) and
website (www.moslengreen.example).
Include: Contaminated Land, Site Remediation, Groundwater Assessment, Health and Ecological Risk Assessments, Acid Sulfate Soils, Waste Classification.

Font styles to use
Serif
Sans Serif

Requirements
Must have
• A creative design different to the standard type of business cards.
Nice to have
• Rounded edges
• Different size of business cards rather than the standard size.
Should not have
• Preferable not to use white colour background, unless it is required from a creative design proposed.
• Not an overloaded design.
• Avoid black colours

```html
<!DOCTYPE html>
<html lang="en">
<head>
<meta charset="utf-8">
<title>MOSLEN Environmental – Business Cards</title>
<link href="https://fonts.googleapis.com/css2?family=Poppins:wght@400;500;600;700&display=swap" rel="stylesheet">
<style>
  :root{
    --backdrop:#1e5226;
    --card-green:#3db851;
    --card-dark:#050505;
    --accent-line:#35b34a;
    --ink-light:#ffffff;
  }
  *{margin:0;padding:0;box-sizing:border-box}
  html,body{width:1200px;height:900px;overflow:hidden}
  body{
    background:var(--backdrop);
    font-family:"Poppins",Arial,sans-serif;
    color:var(--ink-light);
    position:relative;
  }
  .card{
    position:absolute;
    width:560px;height:320px;
    border-radius:30px;
  }
  .card--front{left:80px;top:90px;background:var(--card-green)}
  .card--back{left:560px;top:490px;background:var(--card-dark)}

  .wordmark{
    font-weight:700;
    color:var(--ink-light);
    line-height:1;
    text-align:center;
  }
  .wordmark__name{display:block;letter-spacing:2px}
  .wordmark__sub{display:block;letter-spacing:5px;text-transform:uppercase}

  .card--front .wordmark{position:absolute;left:0;right:0;top:84px}
  .card--front .wordmark__name{font-size:60px}
  .card--front .wordmark__sub{font-size:17px;margin-top:6px}

  .services{
    position:absolute;left:30px;right:30px;bottom:34px;
    text-align:center;font-size:12.5px;font-weight:600;line-height:1.55;
  }

  .card--back .wordmark{position:absolute;right:36px;top:40px}
  .card--back .wordmark__name{font-size:44px}
  .card--back .wordmark__sub{font-size:13px;margin-top:4px;letter-spacing:4px}

  .divider{
    position:absolute;left:36px;right:36px;top:178px;
    height:1px;background:var(--accent-line);
  }
  .person{position:absolute;left:36px;top:124px}
  .person__name{font-size:27px;font-weight:600;line-height:1.05}
  .person__role{font-size:12px;font-weight:500;letter-spacing:1.5px}

  .contacts{position:absolute;left:36px;top:196px;list-style:none}
  .contacts li{display:flex;align-items:center;gap:14px;font-size:12.5px;letter-spacing:1.5px;height:24px}
  .contacts svg{width:15px;height:15px;flex:none}

  .address{
    position:absolute;right:36px;top:196px;
    text-align:right;font-size:12.5px;letter-spacing:1.5px;line-height:1.75;
  }
</style>
</head>
<body>

  <section class="card card--front" aria-label="Card front">
    <div class="wordmark">
      <span class="wordmark__name">MOSLEN</span>
      <span class="wordmark__sub">Environmental</span>
    </div>
    <p class="services">
      Contaminated Land • Site Remediation • Groundwater Assessment<br>
      Health and Ecological Risk Assessments • Acid Sulfate Soils • Waste Classification
    </p>
  </section>

  <section class="card card--back" aria-label="Card back">
    <div class="wordmark">
      <span class="wordmark__name">MOSLEN</span>
      <span class="wordmark__sub">Environmental</span>
    </div>

    <div class="person">
      <p class="person__name">Liam Carver</p>
      <p class="person__role">Managing Director</p>
    </div>

    <div class="divider"></div>

    <ul class="contacts">
      <li>
        <svg viewBox="0 0 16 16" aria-hidden="true"><path fill="#fff" d="M3.6 1.5l2.3 2.6-1.3 1.6c.9 2 2.6 3.7 4.6 4.6l1.6-1.3 2.6 2.3-1.5 2.2C6.8 13.2 2.8 9.2 1.5 3z"/></svg>
        00 987 6543
      </li>
      <li>
        <svg viewBox="0 0 16 16" aria-hidden="true"><rect x="4" y="2" width="8" height="4" fill="#fff"/><rect x="2" y="7" width="12" height="6" rx="1" fill="#fff"/><rect x="5" y="10" width="6" height="4" fill="#050505" stroke="#fff"/></svg>
        00 987 6543
      </li>
      <li>
        <svg viewBox="0 0 16 16" aria-hidden="true"><rect x="1.5" y="3.5" width="13" height="9" fill="none" stroke="#fff" stroke-width="1.4"/><path d="M1.5 3.5L8 9l6.5-5.5" fill="none" stroke="#fff" stroke-width="1.4"/></svg>
        liam@examplesite.example
      </li>
    </ul>

    <p class="address">
      Harlow Park Complex<br>
      Brentvale, Indonesia 40918<br>
      www.examplesite.example
    </p>
  </section>

</body>
</html>
```